Vorlin Diecast Velcor Collectables Website

looking for a vibrant web site marketplace built for diecast car enthusiasts to buy, sell, and trade with ease. Whether you're looking to showcase your own collection or discover rare and exciting models, our site makes the process simple and enjoyable. Clients can browse a curated inventory of high‑quality diecast cars, connect with fellow collectors, and find the perfect pieces to expand their collection. With a smooth user experience and a community-driven spirit, we’re the go‑to destination for anyone passionate about diecast cars.

Target Market(s)

diecast collectors

Industry/Entity Type

Diecast Collectables

Coding

Coded - Design and coding required

Number of Pages Required

3 page

Font styles to use
Sans Serif

Colors
EE7325
F08F49
F5BC92
FAE3D3
FDF4ED

Requirements
Must have
• Cool look and feel. Woo commerce page to post and sell my inventory
Nice to have
• page for users to post their cars or looking for trades.
Should not have
• look cheap

```html
<!DOCTYPE html>
<html lang="en">
<head>
<meta charset="utf-8">
<title>Vorlin Diecast — Buy, Sell &amp; Trade Diecast Cars</title>
<link href="https://fonts.googleapis.com/css2?family=DM+Sans:wght@300;400;500;600;700;800&display=swap" rel="stylesheet">
<style>
:root{
  --orange:#EE7325;
  --orange-2:#F08F49;
  --peach:#F5BC92;
  --cream:#FAE3D3;
  --cream-2:#FDF4ED;
  --ink:#1b1b1b;
  --dark:#141414;
  --dark-2:#1e1e1e;
  --line:#3a3a3a;
  --muted:#5a5a5a;
  --white:#ffffff;
}
*{box-sizing:border-box;margin:0;padding:0}
html,body{width:1200px;height:4630px;overflow:hidden}
body{font-family:"DM Sans",sans-serif;color:var(--ink);background:var(--white);position:relative}
.abs{position:absolute}
section,header,footer{position:absolute;left:0;width:1200px;overflow:hidden}
.eyebrow{font-size:13px;letter-spacing:4px;text-transform:uppercase;font-weight:500}
.btn{position:absolute;display:flex;align-items:center;justify-content:center;font-size:10px;font-weight:600;border-radius:3px}
.btn-orange{background:var(--orange);color:var(--white)}
.btn-outline{border:1px solid #ddd;color:var(--white);background:rgba(255,255,255,.05)}
.photo{position:absolute;border-radius:4px}
.center{left:0;width:1200px;text-align:center}

/* hero */
.hero{top:0;height:681px;background:linear-gradient(100deg,#2a1e14 0%,#3b2a1c 30%,#26211d 55%,#5a2c16 75%,#2a221c 100%)}
.hero .shade{position:absolute;inset:0;background:linear-gradient(180deg,rgba(0,0,0,.45),rgba(0,0,0,.2) 40%,rgba(0,0,0,.55))}
.logo{position:absolute;display:flex;align-items:center;gap:6px;color:var(--white);font-weight:700;font-size:11px;line-height:1.1}
.logo .dot{width:22px;height:22px;border-radius:50%;background:var(--orange)}
.nav{position:absolute;left:383px;top:25px;width:431px;height:36px;border:1px solid rgba(255,255,255,.35);border-radius:20px;background:rgba(40,40,40,.55);display:flex;justify-content:space-around;align-items:center;padding:0 20px;font-size:9.5px;color:var(--white);letter-spacing:.5px}
.hero h1{position:absolute;top:277px;font-size:52px;font-weight:400;color:var(--white)}
.hero p{position:absolute;top:352px;left:260px;width:680px;text-align:center;font-size:12.5px;line-height:1.4;color:#f0f0f0}
.frame-line{position:absolute;height:1px;background:rgba(255,255,255,.35)}

/* about */
.about{top:681px;height:684px;background:var(--white)}
.about h2,.dark h2,.cta h2{font-size:33px;font-weight:400}
.about-card{position:absolute;left:774px;top:151px;width:313px;height:361px;border-radius:6px;background:linear-gradient(160deg,#2e2e2e,#171717);color:#e9e9e9;padding:17px 29px 0 20px;font-size:15px;line-height:21px;font-weight:300}
.stats{position:absolute;left:111px;top:535px;width:976px;height:86px;border-radius:5px;background:linear-gradient(90deg,#2b2b2b,#1d1d1d 60%,#2a2a2a);color:var(--white)}
.stats .lead{position:absolute;left:16px;top:16px;font-size:19px;line-height:1.4;font-weight:400}
.stat{position:absolute;top:20px}
.stat b{display:block;font-size:22px;font-weight:400}
.stat span{font-size:10px;color:#ccc}
.stat-sep{position:absolute;top:26px;width:1px;height:36px;background:#666}

/* dark */
.dark{top:1365px;height:1058px;background:linear-gradient(180deg,#1c1c1c,#111 60%,#181818);color:var(--white)}
.inv-box{position:absolute;left:102px;top:52px;width:994px;height:559px;border:1px solid var(--line);border-radius:6px;background:rgba(255,255,255,.02)}
.car{position:absolute;top:215px;width:219px;height:306px;border-radius:4px;background:#222;overflow:hidden}
.car .img{position:absolute;inset:0;bottom:0}
.car .fade{position:absolute;inset:0;background:linear-gradient(180deg,rgba(0,0,0,0) 45%,rgba(10,10,10,.95) 80%)}
.car h3{position:absolute;left:13px;top:206px;font-size:17px;font-weight:400;white-space:nowrap}
.car .price{position:absolute;left:13px;top:234px;font-size:19px}
.car .view{position:absolute;left:13px;top:269px;width:201px;height:25px;border:1.5px solid #eee;border-radius:2px;font-size:10px;display:flex;align-items:center;justify-content:center}
.arrow-btn{position:absolute;top:545px;width:26px;height:26px;border-radius:50%;background:#2c2c2c;display:flex;align-items:center;justify-content:center}
.steps{position:absolute;left:102px;top:770px;width:994px;height:236px;border:1px solid var(--line);display:flex}
.step{flex:1;border-right:1px solid var(--line);position:relative;padding:0 18px}
.step:last-child{border-right:none}
.step svg{position:absolute;left:18px;top:24px}
.step h4{position:absolute;left:18px;top:148px;font-size:17px;font-weight:400}
.step p{position:absolute;left:18px;top:178px;width:300px;font-size:11.5px;line-height:1.45;color:#ddd}

/* community */
.community{top:2423px;height:499px;background:var(--white)}
.split-h{font-size:34px;font-weight:400;line-height:1.25}
.small-p{font-size:11.5px;line-height:1.4;color:#444}

/* cta */
.cta{top:2922px;height:244px;background:linear-gradient(180deg,#2a2a2a,#121212);color:var(--white)}

/* blogs */
.blogs{top:3166px;height:470px;background:var(--white)}
.blog-title{position:absolute;top:403px;font-size:11.5px;font-weight:600}
.read{position:absolute;top:431px;font-size:9.5px;color:#333}

/* contact */
.contact{top:3636px;height:600px;background:var(--white)}
.form{position:absolute;left:609px;top:30px;width:487px;height:321px;background:#f3f3f3;border-radius:6px;padding:18px}
.form label{position:absolute;left:18px;font-size:10px;font-weight:600}
.field{position:absolute;left:18px;width:451px;background:var(--white);border:1px solid #e2e2e2;border-radius:3px;font-size:9.5px;color:#9a9a9a;padding:9px 12px}
.social{position:absolute;top:328px;width:47px;height:47px;border:1.5px solid #222;border-radius:8px;display:flex;align-items:center;justify-content:center}
.social i{width:14px;height:14px;background:#222;border-radius:3px;display:block}
.insta{position:absolute;top:416px;width:181px;height:179px;border-radius:5px}
.insta .badge{position:absolute;left:12px;top:12px;width:18px;height:18px;border:1.5px solid #fff;border-radius:5px}
.insta.b .badge{top:auto;bottom:12px}

/* footer */
.footer{top:4246px;height:384px;background:#161616;color:var(--white)}
.foot-col h5{font-size:15px;font-weight:400;margin-bottom:10px}
.foot-col a{display:block;font-size:11.5px;color:#6a6a6a;line-height:2}
.news{position:absolute;left:858px;top:71px;width:238px;height:34px;background:#2b2b2b;border-radius:3px;font-size:8px;color:#ccc;padding:12px 10px}
.news .send{position:absolute;right:5px;top:5px;width:24px;height:24px;background:var(--white);border-radius:3px;display:flex;align-items:center;justify-content:center}
.fsocial{position:absolute;top:125px;width:22px;height:22px;background:#fff;border-radius:3px;display:flex;align-items:center;justify-content:center}
.fsocial i{width:8px;height:8px;background:#161616;border-radius:2px;display:block}
.bigword{position:absolute;left:30px;top:150px;font-size:185px;line-height:1;font-weight:800;color:#232323;white-space:nowrap;letter-spacing:-2px}
.copy{position:absolute;top:355px;font-size:11px;color:#ddd}
</style>
</head>
<body>

<header class="hero">
  <div class="photo" style="inset:0;border-radius:0;background:radial-gradient(ellipse at 72% 50%,#b14a1c 0%,#6a2e14 22%,rgba(40,30,24,0) 45%),linear-gradient(180deg,#3a2e24,#1f1a16 60%,#2b2520)" role="img" aria-label="Orange sports car model parked in a display garage diorama"></div>
  <div class="shade"></div>
  <div class="frame-line" style="left:114px;top:637px;width:230px"></div>
  <div class="frame-line" style="left:856px;top:637px;width:230px"></div>
  <div class="logo" style="left:23px;top:20px"><span class="dot"></span><span>Vorlin<br>Diecast</span></div>
  <nav class="nav"><span>HOME</span><span>SHOP</span><span>SELL / TRADE</span><span>COMMUNITY</span><span>ABOUT</span><span>CONTACT</span></nav>
  <div class="btn" style="left:974px;top:30px;width:72px;height:30px;background:#4a4a4a;color:#fff">Login</div>
  <div class="btn btn-orange" style="left:1063px;top:30px;width:110px;height:30px">Sell Your Car</div>
  <div class="abs center eyebrow" style="top:247px;color:#fff;font-size:12px">For Diecast Collectors</div>
  <h1 class="center">Buy, Sell &amp; Trade Diecast Cars</h1>
  <p>Welcome to the ultimate hub for diecast collectors. Explore a growing marketplace where you can buy, sell, or trade your favorite models with collectors from around the world.</p>
  <div class="btn btn-orange" style="left:469px;top:402px;width:133px;height:31px">Browse Inventory</div>
  <div class="btn btn-outline" style="left:616px;top:402px;width:113px;height:31px">List Your Cars</div>
</header>

<section class="about">
  <div class="abs center eyebrow" style="top:64px;font-size:12px">Where Collectors Connect</div>
  <h2 class="abs center" style="top:89px">Built for Collectors, Designed for Passion</h2>
  <div class="photo" style="left:111px;top:151px;width:645px;height:361px;background:linear-gradient(135deg,#6b4a30 0%,#cfcac2 30%,#e7e3dc 55%,#9fb0c0 80%,#c9c4bc)" role="img" aria-label="Hand placing model SUVs and sports cars on a tiled display floor"></div>
  <div class="about-card">A vibrant marketplace built for diecast car enthusiasts to buy, sell, and trade with ease. Discover rare and exciting models, showcase your personal collection, and connect with a growing community of collectors worldwide. Whether you're searching for unique pieces or looking to give your models a new home, our platform makes every interaction simple, smooth, and enjoyable.
    <div class="btn btn-orange" style="left:20px;top:307px;width:149px;height:31px">Explore Marketplace</div>
  </div>
  <div class="stats">
    <div class="lead">Reputation Built on Quality,<br>Transparency &amp; Trust</div>
    <div class="stat" style="left:428px"><b>100%</b><span>Trusted Listings</span></div>
    <div class="stat-sep" style="left:567px"></div>
    <div class="stat" style="left:613px"><b>10,000+</b><span>Diecast Models Listed</span></div>
    <div class="stat-sep" style="left:787px"></div>
    <div class="stat" style="left:834px"><b>500+</b><span>Happy Collectors</span></div>
  </div>
</section>

<section class="dark">
  <div class="inv-box">
    <div class="abs eyebrow" style="left:0;width:992px;text-align:center;top:43px;font-size:12px;color:#ddd">Curated Inventory</div>
    <h2 class="abs" style="left:0;width:992px;text-align:center;top:62px">High-Quality Diecast Cars</h2>
    <p class="abs" style="left:300px;width:392px;text-align:center;top:113px;font-size:11px;line-height:1.4;color:#ddd">Browse a curated inventory of high-quality diecast cars and discover rare and exciting models to expand your collection.</p>
    <div class="car" style="left:32px"><div class="img" role="img" aria-label="Silver and blue model coupe with open hood" style="background:linear-gradient(180deg,#2a2a30,#6d7380 45%,#2a2a2a)"></div><div class="fade"></div><h3>Kazan Strada</h3><div class="price">$45.00</div><div class="view">View Details</div></div>
    <div class="car" style="left:269px"><div class="img" role="img" aria-label="Black supercar model in a showroom" style="background:linear-gradient(180deg,#d8d0b0,#5a5a5a 40%,#222)"></div><div class="fade"></div><h3>Torvani Aventa</h3><div class="price">$60.00</div><div class="view">View Details</div></div>
    <div class="car" style="left:506px"><div class="img" role="img" aria-label="Light blue sports car model in a display shelf" style="background:linear-gradient(180deg,#5a2a2a,#7fa6cc 50%,#2a2a2a)"></div><div class="fade"></div><h3>Rossetta Corsa</h3><div class="price">$55.00</div><div class="view">View Details</div></div>
    <div class="car" style="left:743px"><div class="img" role="img" aria-label="Green sports car model on a display base" style="background:linear-gradient(180deg,#c9c9cc,#3a9a6e 50%,#2a2a2a)"></div><div class="fade"></div><h3>Stuttler Sprint</h3><div class="price">$50.00</div><div class="view">View Details</div></div>
    <div class="arrow-btn" style="left:368px"><svg width="10" height="10" viewBox="0 0 10 10"><path d="M6 2L3 5l3 3" stroke="#999" fill="none" stroke-width="1.3"/></svg></div>
    <div class="btn btn-orange" style="left:424px;top:543px;width:146px;height:30px">View More Featured</div>
    <div class="arrow-btn" style="left:598px"><svg width="10" height="10" viewBox="0 0 10 10"><path d="M4 2l3 3-3 3" stroke="#999" fill="none" stroke-width="1.3"/></svg></div>
  </div>

  <div class="abs center eyebrow" style="top:660px;font-size:12px;color:#ddd">How It Works</div>
  <h2 class="abs center" style="top:688px">Buy, Sell &amp; Trade With Ease</h2>
  <p class="abs center" style="top:738px;font-size:11.5px;color:#ddd">Buy, sell, and trade diecast cars easily through a simple and smooth marketplace experience.</p>
  <div class="steps">
    <div class="step">
      <svg width="68" height="62" viewBox="0 0 68 62" fill="none" stroke="#fff" stroke-width="3.5" stroke-linecap="round" stroke-linejoin="round"><path d="M3 4h10l8 34h36l7-24H17"/><circle cx="25" cy="52" r="5"/><circle cx="52" cy="52" r="5"/></svg>
      <h4>Buy</h4><p>Browse listings and find the perfect diecast model for your collection.</p>
    </div>
    <div class="step">
      <svg width="62" height="62" viewBox="0 0 62 62" fill="none" stroke="#fff" stroke-width="2.5" stroke-linejoin="round"><path d="M6 4h24l10 10v14M6 4v50h22"/><path d="M30 4v10h10"/><path d="M13 24h16M13 32h12M13 40h10"/><circle cx="44" cy="44" r="13"/><path d="M44 51V37M38 43l6-6 6 6"/></svg>
      <h4>Sell</h4><p>List your cars quickly and connect with collectors worldwide.</p>
    </div>
    <div class="step">
      <svg width="52" height="58" viewBox="0 0 52 58" fill="none" stroke="#fff" stroke-width="2.5" stroke-linecap="round" stroke-linejoin="round"><path d="M8 26a18 18 0 0 1 32-12l4 4"/><path d="M44 8v10H34"/><path d="M44 32a18 18 0 0 1-32 12l-4-4"/><path d="M8 50V40h10"/></svg>
      <h4>Trade</h4><p>Exchange models with other collectors and grow your collection.</p>
    </div>
  </div>
</section>

<section class="community">
  <div class="abs eyebrow" style="left:102px;top:63px;font-size:12px">Community</div>
  <h2 class="abs split-h" style="left:102px;top:83px">Join a Community of<br>Passionate Collectors</h2>
  <p class="abs small-p" style="left:596px;top:63px;width:490px">Connect with diecast enthusiasts from around the world and be part of a growing community built on passion and trust. Share your collection, discover rare and exciting models, and interact with collectors who share the same interest. Whether you're looking to showcase your cars or explore new additions, our platform brings collectors together in one place.</p>
  <div class="btn btn-orange" style="left:596px;top:156px;width:149px;height:31px">Join the Community</div>
  <div class="photo" style="left:102px;top:206px;width:492px;height:228px;background:linear-gradient(180deg,#6c6c6c,#c9c9cc 50%,#e4e4e6)" role="img" aria-label="Silver racing coupe model in front of a display cabinet"></div>
  <div class="photo" style="left:614px;top:206px;width:232px;height:228px;background:linear-gradient(135deg,#8a8a88,#c2bfba 45%,#2a3a7a 60%,#d6c0a8)" role="img" aria-label="Hand holding a small dark blue model car"></div>
  <div class="photo" style="left:864px;top:206px;width:232px;height:228px;background:radial-gradient(circle at 55% 50%,#d0342a 0%,#a0281f 25%,#6e6a66 50%,#8e8a86)" role="img" aria-label="Red sports car model with open doors on gravel"></div>
</section>

<section class="cta">
  <div class="abs center eyebrow" style="top:56px;font-size:12px">Get Started</div>
  <h2 class="abs center" style="top:78px">Your Next Great Find Is Waiting</h2>
  <p class="abs center" style="top:131px;font-size:11.5px;color:#ddd">Browse our inventory, list your own cars, or connect with fellow collectors to find the perfect addition to your collection.</p>
  <div class="btn btn-orange" style="left:472px;top:166px;width:134px;height:31px">Browse Inventory</div>
  <div class="btn btn-outline" style="left:619px;top:166px;width:108px;height:31px;background:#3a3a3a;border-color:#777">Start Selling</div>
</section>

<section class="blogs">
  <div class="abs eyebrow" style="left:102px;top:73px;font-size:12px">Latest Blogs</div>
  <h2 class="abs" style="left:102px;top:99px;font-size:34px;font-weight:400">Insights for Diecast Collectors</h2>
  <p class="abs small-p" style="left:596px;top:73px;width:460px">Explore tips, guides, and insights to help you grow and manage your diecast collection.</p>
  <div class="btn btn-orange" style="left:596px;top:117px;width:130px;height:31px">View More Blogs</div>
  <div class="photo" style="left:102px;top:166px;width:320px;height:212px;background:linear-gradient(135deg,#d8342a,#2a62c4 30%,#e8c23a 55%,#2a9a5a 75%,#c43a8a)" role="img" aria-label="Pile of colorful diecast cars"></div>
  <div class="photo" style="left:440px;top:166px;width:320px;height:212px;background:linear-gradient(180deg,#c7b9a2,#3a72b8 30%,#d7c8b0 50%,#c4362a 70%,#d2c4ac)" role="img" aria-label="Rows of small diecast cars arranged on a shelf"></div>
  <div class="photo" style="left:778px;top:166px;width:318px;height:212px;background:linear-gradient(180deg,#c7a27a,#2a2a2a 40%,#2a7a4a 70%,#b8946c)" role="img" aria-label="Black and green vintage model cars held in hand"></div>
  <div class="blog-title" style="left:104px">Top 10 Rare Diecast Cars Every Collector Wants</div>
  <div class="blog-title" style="left:442px">Beginner's Guide to Starting a Diecast Collection</div>
  <div class="blog-title" style="left:780px">How to Spot Authentic vs. Replica Diecast Models</div>
  <div class="read" style="left:106px">Read More &nbsp;↗</div>
  <div class="read" style="left:444px">Read More &nbsp;↗</div>
  <div class="read" style="left:781px">Read More &nbsp;↗</div>
</section>

<section class="contact">
  <div class="abs eyebrow" style="left:102px;top:32px;font-size:12px">Contact Us</div>
  <h2 class="abs" style="left:102px;top:57px;font-size:34px;font-weight:400;line-height:1.3">Get in Touch with Our<br>Team</h2>
  <p class="abs small-p" style="left:102px;top:159px;width:470px">Have questions about buying, selling, or trading diecast cars? Our team is here to help. Whether you need support with your listings, want to learn more about the platform, or simply want to connect with us, feel free to reach out. We're ready to assist you and make your experience smooth and enjoyable.</p>
  <div class="social" style="left:102px"><i></i></div>
  <div class="social" style="left:162px"><i></i></div>
  <div class="social" style="left:222px"><i></i></div>
  <div class="form">
    <label style="top:17px">Name</label>
    <div class="field" style="top:37px;height:32px">Please enter your name.</div>
    <label style="top:78px">Email</label>
    <div class="field" style="top:97px;height:32px">Please enter your email ID.</div>
    <label style="top:138px">Message</label>
    <div class="field" style="top:158px;height:95px">Please write your message here.</div>
    <div class="btn btn-orange" style="left:18px;top:268px;width:120px;height:33px;font-size:11px;font-weight:500">Submit Now</div>
  </div>
  <div class="insta" style="left:23px;background:linear-gradient(180deg,#5a5450,#c49a5a 60%,#6a5e54)" role="img" aria-label="Yellow compact car model"><span class="badge"></span></div>
  <div class="insta b" style="left:219px;background:linear-gradient(180deg,#8a6a4a,#e0ddd8 60%,#7a6a5a)" role="img" aria-label="White rally car model"><span class="badge"></span></div>
  <div class="insta" style="left:414px;background:linear-gradient(180deg,#5a5a5a,#2a8a4a 60%,#c83a2a)" role="img" aria-label="Green stock car model held in hand"><span class="badge"></span></div>
  <div class="insta b" style="left:609px;background:linear-gradient(180deg,#3a4a6a,#c83a3a 50%,#9a9aa0)" role="img" aria-label="Row of red and silver sports car models"><span class="badge"></span></div>
  <div class="insta" style="left:804px;background:linear-gradient(180deg,#3a3a4a,#b8323a 50%,#a0a0a8)" role="img" aria-label="Group of sports car models on a table"><span class="badge"></span></div>
  <div class="insta b" style="left:996px;width:181px;background:linear-gradient(180deg,#3a5a8a,#e8a23a 50%,#5a4a3a)" role="img" aria-label="Yellow and orange model cars on display"><span class="badge"></span></div>
</section>

<footer class="footer">
  <div class="bigword">Vorlin Diecast</div>
  <div class="abs" style="left:108px;top:48px;display:flex;align-items:center;gap:8px"><span style="width:30px;height:30px;border-radius:50%;background:var(--orange);display:block"></span><span style="font-size:15px;font-weight:700">Vorlin Diecast</span></div>
  <div class="abs foot-col" style="left:334px;top:40px"><h5>Quick Links</h5><a>Home</a><a>Shop</a><a>Sell / Trade</a><a>Community</a><a>About</a></div>
  <div class="abs foot-col" style="left:548px;top:40px"><h5>Services</h5><a>Contact</a><a>Privacy Policy</a><a>Terms &amp; Conditions</a><a>FAQs</a></div>
  <div class="abs foot-col" style="left:858px;top:40px"><h5>Newsletter</h5></div>
  <div class="news">Your Email Address<span class="send"><svg width="14" height="14" viewBox="0 0 14 14"><path d="M1 7l12-6-4 12-2-5z" fill="#161616"/></svg></span></div>
  <div class="fsocial" style="left:860px"><i></i></div>
  <div class="fsocial" style="left:896px"><i></i></div>
  <div class="fsocial" style="left:932px"><i></i></div>
  <div class="copy center">© 2026 <b>Vorlin Diecast</b>. All rights reserved</div>
</footer>

</body>
</html>
```